Property inspection company needs logo/business card design

A new, home, commercial, and multi dwelling inspection company needs help with a new logo and hence business cards.

Time is extended for the rest of the week.

Font styles to use
Sans Serif

Colors
ec1f27
0255a3
ffffff

```html
<!DOCTYPE html>
<html lang="en">
<head>
<meta charset="UTF-8">
<title>Reed Halloway Property Inspections – Business Cards</title>
<link rel="stylesheet" href="https://fonts.googleapis.com/css2?family=Montserrat:wght@600&family=Open+Sans:wght@400&display=swap">
<style>
  :root {
    --red: #ec1f27;
    --blue: #0255a3;
    --white: #ffffff;
    --ink: #222222;
    --backdrop: #e9eaec;
  }
  * { margin: 0; padding: 0; box-sizing: border-box; }
  html, body { width: 1200px; height: 895px; overflow: hidden; }
  body {
    background: var(--backdrop);
    font-family: "Open Sans", sans-serif;
    position: relative;
  }
  .card {
    position: absolute;
    top: 97px;
    width: 400px;
    height: 700px;
    overflow: hidden;
  }
  .card--front { left: 160px; background: var(--blue); }
  .card--back  { left: 640px; background: var(--white); }

  .frame {
    position: absolute;
    left: 110px;
    top: 40px;
    width: 260px;
    height: 300px;
  }
  .frame svg { display: block; }

  .identity {
    position: absolute;
    left: 110px;
    top: 160px;
  }
  .identity__name {
    font-family: "Montserrat", sans-serif;
    font-weight: 600;
    font-size: 25px;
    letter-spacing: 0.5px;
    color: var(--red);
    line-height: 1.1;
    white-space: nowrap;
  }
  .identity__role {
    font-size: 15px;
    line-height: 1.4;
    white-space: nowrap;
  }
  .card--front .identity__role { color: var(--white); }
  .card--back  .identity__role { color: var(--ink); }

  .contact {
    position: absolute;
    left: 40px;
    top: 430px;
    color: var(--ink);
  }
  .contact__icons { display: flex; gap: 6px; margin-bottom: 6px; }
  .contact__phone { font-size: 24px; line-height: 1.2; }
  .contact__email { font-size: 16px; line-height: 1.5; }

  .web {
    position: absolute;
    left: 40px;
    top: 530px;
  }
  .web__rule {
    width: 70px;
    height: 2px;
    background: var(--red);
    margin-bottom: 12px;
  }
  .web__url { font-size: 17px; white-space: nowrap; }
  .card--front .web { top: 520px; }
  .card--front .web__url { color: var(--white); }
  .card--back .web { top: 515px; }
  .card--back .web__url { color: var(--ink); }
</style>
</head>
<body>

  <!-- Front: blue -->
  <section class="card card--front">
    <div class="frame">
      <svg width="260" height="300" viewBox="0 0 260 300">
        <polyline points="1,110 1,1 259,1 259,299 1,299 1,200" fill="none" stroke="var(--red)" stroke-width="2"/>
      </svg>
    </div>
    <div class="identity">
      <div class="identity__name">REED HALLOWAY</div>
      <div class="identity__role">Property Inspections Inc.</div>
    </div>
    <div class="web">
      <div class="web__rule"></div>
      <div class="web__url">www.ReedHalloway.com</div>
    </div>
  </section>

  <!-- Back: white -->
  <section class="card card--back">
    <div class="frame">
      <svg width="260" height="300" viewBox="0 0 260 300">
        <polyline points="1,110 1,1 259,1 259,299 1,299 1,200" fill="none" stroke="var(--blue)" stroke-width="2"/>
      </svg>
    </div>
    <div class="identity">
      <div class="identity__name">MARCUS ELLISON</div>
      <div class="identity__role">Founder &amp; CEO</div>
    </div>
    <div class="contact">
      <div class="contact__icons">
        <svg class="icon icon--phone" width="18" height="18" viewBox="0 0 24 24" aria-label="Phone">
          <path d="M6.6 10.8a15.1 15.1 0 0 0 6.6 6.6l2.2-2.2a1 1 0 0 1 1-.25 11.4 11.4 0 0 0 3.6.57 1 1 0 0 1 1 1V20a1 1 0 0 1-1 1A17 17 0 0 1 3 4a1 1 0 0 1 1-1h3.5a1 1 0 0 1 1 1c0 1.25.2 2.45.57 3.6a1 1 0 0 1-.25 1z" fill="var(--red)"/>
        </svg>
        <svg class="icon icon--mail" width="20" height="18" viewBox="0 0 24 20" aria-label="Email">
          <rect x="1" y="2" width="22" height="16" rx="2" fill="var(--red)"/>
          <polyline points="2,4 12,11 22,4" fill="none" stroke="var(--white)" stroke-width="2"/>
        </svg>
      </div>
      <div class="contact__phone">000-000-0000</div>
      <div class="contact__email">m_ellison@ReedHalloway.com</div>
    </div>
    <div class="web">
      <div class="web__rule"></div>
      <div class="web__url">www.ReedHalloway.com</div>
    </div>
  </section>

</body>
</html>
```